Vital Spark Electrical in need of a business card design

We need a new business card designed for our electrical business. We have a logo already which I will attach below.
Would like the business card to be..
-BLACK background preferably, possibly white back ground behind logo if colours clash.
-White & Blue (logo blue) text
Something that makes the logo pop, & a modern look. Possibly minimal clean format.

REQUIRE:
-Logo on front & back

TEXT TO INCLUDE (ON ONE SIDE):

Tom Harlow
Director/Electrician
M: 0417 365 208
E:info@vitalsparkelectrical-example.com.au
W:www.vitalsparkelectrical-example.com.au
R.E.C 57318

Custom/New Homes
Renovations
Commercial Office/Shop Fit-outs
Communications & Security Cameras
Electric Vehicle Chargers
Airconditioning
Updates

Requirements
Nice to have
• Possibly even lighten the grey shades for the words 'Vital' & 'Spark' to be more easily read on a black background.

```html
<!DOCTYPE html>
<html lang="en">
<head>
<meta charset="utf-8">
<title>Vital Spark Electrical – Business Card</title>
<link rel="stylesheet" href="https://fonts.googleapis.com/css2?family=Ubuntu:wght@400;500&family=Lato:wght@400&family=Arimo:wght@400&display=swap">
<style>
  :root {
    --page: #b3b3b3;
    --card: #0b0b0b;
    --blue: #00a6e0;
    --white: #ffffff;
  }
  * { box-sizing: border-box; margin: 0; padding: 0; }
  html, body { width: 1200px; height: 976px; overflow: hidden; }
  body { background: var(--page); position: relative; }

  .card {
    position: absolute;
    left: 285px;
    width: 630px;
    height: 360px;
    background: var(--card);
    overflow: hidden;
  }
  .card--front { top: 115px; }
  .card--back { top: 500px; }

  .brand {
    position: absolute;
    display: flex;
    align-items: center;
    color: var(--white);
    font-family: "Ubuntu", sans-serif;
    font-weight: 500;
    line-height: 1.05;
  }
  .brand__mark { background: var(--blue); flex: none; }
  .card--front .brand { left: 38px; top: 150px; font-size: 27px; gap: 16px; }
  .card--front .brand__mark { width: 52px; height: 52px; }
  .card--back .brand { left: 114px; top: 123px; font-size: 44px; gap: 26px; }
  .card--back .brand__mark { width: 84px; height: 84px; }

  .divider {
    position: absolute;
    left: 315px; top: 111px;
    width: 1px; height: 139px;
    background: var(--white);
  }

  .contact { position: absolute; left: 342px; top: 106px; }
  .contact__name {
    font-family: "Ubuntu", sans-serif;
    font-size: 26px; color: var(--blue);
    line-height: 30px;
  }
  .contact__role {
    font-family: "Lato", sans-serif;
    font-size: 14.5px; color: var(--white);
    margin-top: 1px;
  }
  .contact__list { list-style: none; margin-top: 18px; }
  .contact__item {
    display: flex; align-items: center; gap: 5px;
    font-family: "Lato", sans-serif;
    font-size: 12.5px; color: var(--white);
    line-height: 20px;
  }
  .contact__item svg { width: 11px; height: 11px; flex: none; }
  .contact__licence {
    font-family: "Ubuntu", sans-serif;
    font-size: 15px; color: var(--blue);
    margin-top: 3px;
  }

  .band { position: absolute; left: 0; bottom: 0; width: 630px; height: 11px; }

  .services {
    position: absolute; left: 0; right: 0; top: 288px;
    text-align: center;
    font-family: "Arimo", sans-serif;
    font-size: 15px; line-height: 20px;
    color: var(--white);
  }
  .services__sep { color: var(--blue); padding: 0 2px; }
</style>
</head>
<body>

<section class="card card--front">
  <div class="brand">
    <span class="brand__mark"></span>
    <span class="brand__name">Vital Spark<br>Electrical</span>
  </div>

  <span class="divider"></span>

  <div class="contact">
    <h1 class="contact__name">Tom Harlow</h1>
    <p class="contact__role">Director/Electrician</p>
    <ul class="contact__list">
      <li class="contact__item">
        <svg viewBox="0 0 12 12"><rect x="3" y="0.5" width="6" height="11" rx="1" fill="none" stroke="var(--blue)" stroke-width="1.2"/><circle cx="6" cy="9.6" r="0.6" fill="var(--blue)"/></svg>
        0417 365 208
      </li>
      <li class="contact__item">
        <svg viewBox="0 0 12 12"><rect x="0.5" y="2.5" width="11" height="7" fill="var(--blue)"/><path d="M0.5 2.5 6 6.5 11.5 2.5" fill="none" stroke="var(--card)" stroke-width="1"/></svg>
        info@vitalsparkelectrical-example.com.au
      </li>
      <li class="contact__item">
        <svg viewBox="0 0 12 12" fill="none" stroke="var(--blue)" stroke-width="0.9"><circle cx="6" cy="6" r="5.2"/><ellipse cx="6" cy="6" rx="2.3" ry="5.2"/><path d="M0.8 6h10.4M1.7 3.3h8.6M1.7 8.7h8.6"/></svg>
        www.vitalsparkelectrical-example.com.au
      </li>
    </ul>
    <p class="contact__licence">R.E.C 57318</p>
  </div>

  <svg class="band" viewBox="0 0 630 11" preserveAspectRatio="none" aria-hidden="true">
    <polygon points="0,0 318,0 306,11 0,11" fill="var(--blue)"/>
    <polygon points="322,0 630,0 630,11 310,11" fill="var(--white)"/>
  </svg>
</section>

<section class="card card--back">
  <div class="brand">
    <span class="brand__mark"></span>
    <span class="brand__name">Vital Spark<br>Electrical</span>
  </div>

  <p class="services">
    Custom/New Homes <span class="services__sep">|</span> Renovations <span class="services__sep">|</span> Commercial Office/Shop Fit-outs<br>
    Communications &amp; Security Cameras <span class="services__sep">|</span> Electric Vehicle Chargers <span class="services__sep">|</span> Airconditioning
  </p>
</section>

</body>
</html>
```